Tobias Wrenfield Business Card

In addition to my name design (file uploaded), black print on white card stock, e-mail address should be presented as a typical e-mail address, i.e., underlined and in blue ink, the card should include the following information:
Professor of Aviation Technology
Accident Litigation Expert Witness
Master Certificated Flight Instructor

twrenfield@qorvanet.net
Anchorage, Alaska
(907) 518-2736

Industry/Entity Type

Business

```html
<!DOCTYPE html>
<html lang="en">
<head>
<meta charset="utf-8">
<title>Tobias E. Wrenfield — Business Card</title>
<link rel="stylesheet" href="https://fonts.googleapis.com/css2?family=Barlow+Semi+Condensed:wght@600&family=Tinos&display=swap">
<style>
  :root {
    --frame: #dde3e1;
    --card: #ffffff;
    --ink: #111111;
    --rule: #b8bfbe;
    --link: #2a4fe0;
  }
  html, body {
    margin: 0;
    padding: 0;
    width: 1200px;
    height: 857px;
    overflow: hidden;
    background: var(--frame);
  }
  .card {
    position: absolute;
    left: 11px;
    top: 11px;
    width: 1178px;
    height: 835px;
    background: var(--card);
    color: var(--ink);
  }
  .card__name {
    position: absolute;
    left: 60px;
    top: 103px;
    margin: 0;
    font-family: "Barlow Semi Condensed", "Arial Narrow", sans-serif;
    font-weight: 600;
    font-size: 50px;
    line-height: 1;
    letter-spacing: 0.5px;
    text-transform: uppercase;
  }
  .card__rule {
    position: absolute;
    left: 60px;
    top: 173px;
    width: 1097px;
    height: 1px;
    background: var(--rule);
  }
  .card__titles,
  .card__contact {
    position: absolute;
    left: 411px;
    margin: 0;
    padding: 0;
    list-style: none;
    font-family: "Tinos", "Times New Roman", serif;
    font-size: 43px;
    line-height: 66px;
  }
  .card__titles { top: 213px; }
  .card__contact { top: 493px; }
  .card__email {
    color: var(--link);
    text-decoration: underline;
    text-decoration-thickness: 1px;
    text-underline-offset: 9px;
  }
</style>
</head>
<body>
  <main class="card">
    <h1 class="card__name">Tobias E. Wrenfield</h1>
    <div class="card__rule"></div>
    <ul class="card__titles">
      <li>Professor of Aviation Technology</li>
      <li>Accident Litigation Expert Witness</li>
      <li>Master Certificated Flight Instructor</li>
    </ul>
    <ul class="card__contact">
      <li><a class="card__email" href="mailto:twrenfield@qorvanet.net">twrenfield@qorvanet.net</a></li>
      <li>Anchorage, Alaska</li>
      <li>(907) 518-2736</li>
    </ul>
  </main>
</body>
</html>
```